stationary design
Brightway Journeys
Project: stationary design
stationary design - Travel
Creative Brief
Professional
Ibrahim Naseer
Managing Director
H. Fehimaage, Kanbaafaru Higun, Male' Maldives.
naseer@brightwayjourney.example
www.brightwayjourney.example

```html
<!DOCTYPE html>
<html lang="en">
<head>
<meta charset="utf-8">
<title>Brightway Journeys – Stationery</title>
<link rel="stylesheet" href="https://fonts.googleapis.com/css2?family=PT+Serif:wght@400;700&display=swap">
<style>
  :root {
    --navy: #1f3a78;
    --orange: #f29a1f;
    --paper: #ffffff;
    --ink: #2b2b2b;
    --muted: #6b6b6b;
    --rule: #c9c9c9;
    --backdrop: #e6e7ea;
  }
  * { box-sizing: border-box; margin: 0; padding: 0; }
  html, body { width: 1200px; height: 869px; overflow: hidden; }
  body {
    background: var(--backdrop);
    font-family: "PT Serif", Georgia, serif;
    color: var(--ink);
    position: relative;
  }
  .card {
    position: absolute;
    width: 520px;
    height: 300px;
    border-radius: 16px;
    overflow: hidden;
    box-shadow: 0 6px 18px rgba(0,0,0,.18);
  }
  .card--front { left: 380px; top: 70px; background: var(--paper); }
  .card--plain { left: 110px; top: 480px; background: var(--paper); }
  .card--blue  { left: 650px; top: 480px; background: var(--navy); }

  .wordmark {
    position: absolute;
    font-weight: 400;
    text-transform: uppercase;
    letter-spacing: 1px;
    line-height: 1.05;
    color: var(--navy);
  }
  .card--front .wordmark { left: 30px; top: 100px; font-size: 28px; }
  .card--plain .wordmark { left: 0; right: 0; top: 112px; text-align: center; font-size: 34px; }
  .card--blue .wordmark  { left: 0; right: 0; top: 112px; text-align: center; font-size: 34px; color: var(--paper); }

  .divider {
    position: absolute;
    left: 282px; top: 34px;
    width: 1px; height: 180px;
    background: var(--rule);
  }
  .contact {
    position: absolute;
    left: 296px; top: 34px;
    font-size: 10.5px;
    line-height: 1.45;
    white-space: nowrap;
  }
  .contact__name { font-size: 17px; font-weight: 700; color: var(--navy); line-height: 1.2; }
  .contact__title { color: var(--muted); margin-bottom: 16px; }
  .contact__address { margin-bottom: 16px; }

  .footer-band {
    position: absolute;
    left: 0; right: 0; bottom: 0;
    height: 44px;
    background: var(--navy);
    border-top: 4px solid var(--orange);
    display: flex;
    align-items: center;
    justify-content: center;
  }
  .footer-band__web {
    color: var(--paper);
    font-size: 11px;
    letter-spacing: 2.5px;
  }
</style>
</head>
<body>

  <section class="card card--front" aria-label="Business card front">
    <p class="wordmark">Brightway<br>Journeys</p>
    <span class="divider"></span>
    <div class="contact">
      <p class="contact__name">Ibrahim Naseer</p>
      <p class="contact__title">Managing Director</p>
      <p class="contact__address">H. Fehimaage, Kanbaafaru Higun,<br>Male' Maldives.</p>
      <p>Phone: +960 300 1122</p>
      <p>Cell: +960 700 4455</p>
      <p>Fax: +960 300 7788</p>
      <p>Email: naseer@brightwayjourney.example</p>
    </div>
    <div class="footer-band">
      <span class="footer-band__web">www.brightwayjourney.example</span>
    </div>
  </section>

  <section class="card card--plain" aria-label="Business card back, white">
    <p class="wordmark">Brightway<br>Journeys</p>
  </section>

  <section class="card card--blue" aria-label="Business card back, blue">
    <p class="wordmark">Brightway<br>Journeys</p>
  </section>

</body>
</html>
```